Business card for a shop called "Bright loom company"

the shop are selling disposable wooden packaging cutlery, wooden trays, wooden plates, carton, box, adhesive, stretch film...
Fully recyclable and 100% wood.
We want something futuristic and good for the planet

Target Market(s)

professional customers, company, fast-food, restaurant, caterer,

Industry/Entity Type

wood furnitures for food

Contact Information for Business Card

Colors

Designer to choose colors to be used in the design.

Requirements
Must have
• QR CODE, selective varnish on the given logo, brown and neon green light color. Name and surname, function (CEO), tel, mail and address.
Nice to have
• minimalist design , futuristic and ecology
Should not have
• the list of furniture we are selling.

```html
<!DOCTYPE html>
<html lang="en">
<head>
<meta charset="utf-8">
<title>Bright loom company – Business card</title>
<link rel="stylesheet" href="https://fonts.googleapis.com/css2?family=Lato:wght@400;700&family=Oswald:wght@500&family=Archivo:wght@500&display=swap">
<style>
  :root {
    --page: #0c0c0c;
    --card: #1b1b1b;
    --band: #8a6414;
    --green: #1fae3c;
    --neon: #4cf06a;
    --ink: #f2f2f2;
    --rule: #8a8a8a;
  }
  * { box-sizing: border-box; margin: 0; padding: 0; }
  html, body { width: 1200px; height: 900px; overflow: hidden; }
  body {
    background: var(--page);
    display: flex; flex-direction: column; align-items: center; justify-content: center;
    gap: 40px;
    font-family: "Lato", sans-serif;
  }
  .card {
    position: relative;
    width: 700px; height: 400px;
    background: var(--card);
    box-shadow: 0 10px 30px rgba(0,0,0,.6);
    overflow: hidden;
  }
  .card::after {
    content: ""; position: absolute; left: 0; right: 0; bottom: 0;
    height: 12px; background: var(--band);
  }

  /* Front */
  .brand {
    position: absolute; left: 255px; top: 70px;
    width: 330px; height: 200px;
    display: flex; align-items: center; justify-content: center; gap: 20px;
  }
  .brand-mark {
    width: 64px; height: 64px; border-radius: 50%;
    background: var(--band); flex: none;
  }
  .brand-name {
    font-family: "Lato", sans-serif; font-weight: 700;
    font-size: 48px; line-height: 1.05; color: var(--neon);
  }
  .recycle-badge {
    position: absolute; left: 78px; top: 262px;
    display: flex; flex-direction: column; align-items: center; gap: 6px;
  }
  .recycle-badge .badge { width: 50px; height: 50px; border-radius: 50%; background: var(--green); }
  .recycle-badge .badge-label { font-size: 6px; font-weight: 700; color: var(--green); letter-spacing: .3px; }
  .tagline {
    position: absolute; left: 150px; bottom: 26px;
    font-family: "Archivo", sans-serif; font-weight: 500;
    font-size: 22px; letter-spacing: 1px; color: var(--ink);
  }

  /* Back */
  .person { position: absolute; left: 85px; top: 125px; text-align: right; width: 285px; }
  .person-name {
    font-family: "Oswald", sans-serif; font-weight: 500;
    font-size: 46px; color: var(--green); line-height: 1; text-transform: uppercase;
    letter-spacing: -.5px;
  }
  .person-role { font-size: 22px; color: var(--ink); margin-top: 4px; }
  .divider {
    position: absolute; left: 395px; top: 125px;
    width: 1px; height: 95px; background: var(--rule);
  }
  .contacts { position: absolute; left: 420px; top: 140px; list-style: none; }
  .contacts li {
    display: flex; align-items: center; gap: 12px;
    font-size: 21px; color: var(--ink); line-height: 32px;
  }
  .contacts svg { width: 20px; height: 20px; fill: var(--green); flex: none; }
  .address {
    position: absolute; left: 95px; bottom: 36px;
    font-size: 23px; color: var(--ink);
  }
</style>
</head>
<body>

<section class="card card-front">
  <div class="brand">
    <span class="brand-mark"></span>
    <span class="brand-name">Bright loom<br>company</span>
  </div>
  <div class="recycle-badge">
    <span class="badge"></span>
    <span class="badge-label">100% RECYCLABLE</span>
  </div>
  <p class="tagline">FULLY RECYCLABLE AND 100% WOOD</p>
</section>

<section class="card card-back">
  <div class="person">
    <h1 class="person-name">Daniel Carter</h1>
    <p class="person-role">Managing Director</p>
  </div>
  <span class="divider"></span>
  <ul class="contacts">
    <li>
      <svg viewBox="0 0 24 24" aria-hidden="true"><path d="M6.6 10.8a15.1 15.1 0 0 0 6.6 6.6l2.2-2.2c.3-.3.7-.4 1-.2 1.1.4 2.3.6 3.6.6.6 0 1 .4 1 1V20c0 .6-.4 1-1 1A17 17 0 0 1 3 4c0-.6.4-1 1-1h3.5c.6 0 1 .4 1 1 0 1.3.2 2.5.6 3.6.1.3 0 .7-.2 1z"/></svg>
      044-987 654 321
    </li>
    <li>
      <svg viewBox="0 0 24 24" aria-hidden="true"><path d="M2 5h20v14H2z M2 5l10 8 10-8" fill="none" stroke="#1fae3c" stroke-width="2"/><path d="M2 5l10 8 10-8z"/></svg>
      info@brightloom.com
    </li>
    <li>
      <svg viewBox="0 0 24 24" aria-hidden="true"><circle cx="12" cy="12" r="9" fill="none" stroke="#1fae3c" stroke-width="2"/><path d="M3 12h18M12 3c3 3 3 15 0 18M12 3c-3 3-3 15 0 18" fill="none" stroke="#1fae3c" stroke-width="1.6"/></svg>
      www.brightloom.com
    </li>
  </ul>
  <p class="address">18, Market Street, Harbor City, 30117</p>
</section>

</body>
</html>
```